Business card design needed

Family General Practitioner/ Family Physician.
Logo is the logo of the Crestmoor Guild of Family Clinicians Australia
http://kvplm.tarevo.edu.au/PictureGallery/logos/pages/CGFC%20logo_jpg.htm

Reason: Just a bit more time to make changes and the weekend for me to look at things closely and to choose. Thanks, Lumi

Thanks for all the submissions. So many of them are really works of art. Not one of them are not good. The ones that I am eliminating are the ones that I think are not suitable for me personally only, and because if I don't, it makes it very difficult to decide as many of you are also sending me slight variations of a card. I have just decided to choose a second place card too. Can't thank you all enough. Good luck, Lumi. P.S - Working today till 10 pm as the card says :-), so probably won't be able to give a feedback till late Saturday night or Sunday morning here in Sydney, Australia. 

Reason: Just added a second place to the budget and realised that Australia is ahead of the rest of the world in the time zone (only :-) - don't want to offend anyone or start a debate!! ) , so Monday deadline will mean it will be a weekend for the rest of the world. Just wanted to give everyone more time to submit their best, especially since I will be picking a second card too. Can't thank everyone enough for the submissions. P.S - Not keen on photos on the card.

Contact Information for Business Card

Dr. Lumi Harcourt M.B.B.S., F.C.G.F.C
Family General Practitioner
Address, timings, phone and fax number on the back.

Requirements
Must have
• Timings
Mon 7 am - 7 pm
Tues 7 am - 12 pm
Wed 7 am - 10 pm
Thurs 7 am - 12 pm
Fri 7 am - 8 pm
Sat 8 am - 10 pm
Sun - Off

```html
<!DOCTYPE html>
<html lang="en">
<head>
<meta charset="utf-8">
<title>Dr. Lumi Harcourt – Business Card</title>
<link rel="stylesheet" href="https://fonts.googleapis.com/css2?family=Cinzel:wght@400;500&family=Open+Sans:wght@400;600;700;800&family=Tinos:wght@400;700&display=swap">
<style>
  :root {
    --page: #efece6;
    --blue-deep: #2f5499;
    --blue-light: #3cb9da;
    --orange: #f07a22;
    --yellow: #fdc43a;
    --purple: #7b2b72;
    --red: #e8402e;
    --white: #ffffff;
    --label: #ffffff;
    --label-bg: #5b4a3b;
  }
  * { box-sizing: border-box; margin: 0; padding: 0; }
  html, body { width: 1200px; height: 739px; overflow: hidden; }
  body { background: var(--page); position: relative; font-family: "Open Sans", sans-serif; color: var(--white); }

  .card {
    position: absolute; width: 525px; height: 300px; overflow: hidden;
    background: linear-gradient(90deg, var(--blue-deep) 0%, #3a7fbe 55%, var(--blue-light) 100%);
    box-shadow: 0 2px 6px rgba(0,0,0,.25);
  }
  .card--front { left: 40px; top: 28px; }
  .card--opt1 { left: 615px; top: 27px; }
  .card--opt2 { left: 47px; top: 368px; }
  .card--opt3 { left: 612px; top: 376px; }

  /* front */
  .front-waves { position: absolute; inset: 0; }
  .doctor-name {
    position: absolute; top: 30px; left: 0; width: 525px; text-align: center;
    font-family: "Cinzel", serif; font-size: 42px; letter-spacing: 1px; font-weight: 500;
  }
  .credentials {
    position: absolute; top: 83px; width: 525px; text-align: center;
    font-family: "Tinos", serif; font-size: 11px; letter-spacing: .5px;
  }
  .role {
    position: absolute; top: 122px; width: 525px; text-align: center;
    font-family: "Tinos", serif; font-size: 19px; letter-spacing: 2px;
  }
  .tagline {
    position: absolute; left: 113px; top: 266px;
    font-family: "Tinos", serif; font-weight: 700; font-size: 23px;
  }
  .guild-mark {
    position: absolute; left: 410px; top: 246px; display: flex; align-items: center; gap: 5px;
    font-family: "Tinos", serif; font-weight: 700; font-size: 18px; color: var(--white);
  }
  .guild-mark .dot { width: 14px; height: 14px; border-radius: 50%; background: var(--white); }

  /* back */
  .faint-mark {
    position: absolute; right: 40px; top: 70px;
    font-family: "Open Sans", sans-serif; font-weight: 700; font-size: 62px;
    color: rgba(255,255,255,.09); letter-spacing: 2px;
  }
  .hours-title { position: absolute; font-size: 20px; font-weight: 400; }
  .hours { position: absolute; list-style: none; font-size: 16.5px; }
  .hours li { height: 23px; line-height: 23px; white-space: pre; }
  .hours .time { font-weight: 700; }

  .card--opt1 .hours-title { left: 38px; top: 16px; }
  .card--opt1 .hours { left: 38px; top: 44px; font-weight: 700; text-transform: uppercase; }

  .card--opt2 .hours-title { left: 51px; top: 6px; letter-spacing: 1px; }
  .card--opt2 .hours { left: 31px; top: 42px; }
  .card--opt2 .hours li { display: flex; }
  .card--opt2 .hours .day { width: 109px; }

  .card--opt3 .hours-title { left: 37px; top: 16px; }
  .card--opt3 .hours { left: 37px; top: 45px; }

  .contact-band {
    position: absolute; left: 0; bottom: 0; width: 525px; height: 77px;
    background: linear-gradient(90deg, var(--orange), var(--yellow));
    border-top: 2px solid rgba(255,255,255,.55);
    font-family: "Tinos", serif; text-align: center; font-size: 15.5px; line-height: 18px;
    padding-top: 6px;
  }
  .contact-band .phones { margin-top: 9px; display: flex; justify-content: center; gap: 10px; }
  .contact-band .sep { border-left: 1.5px solid var(--white); height: 18px; }

  .option-label {
    position: absolute; font-family: "Open Sans", sans-serif; font-weight: 800; font-size: 20px;
    color: var(--label-bg);
  }
</style>
</head>
<body>

<section class="card card--front" aria-label="Card front">
  <svg class="front-waves" viewBox="0 0 525 300" width="525" height="300">
    <defs>
      <linearGradient id="warm" x1="0" x2="1" y1="0" y2="0">
        <stop offset="0" stop-color="#f07a22"/>
        <stop offset="1" stop-color="#fdc43a"/>
      </linearGradient>
    </defs>
    <path d="M0,262 C160,272 300,215 525,160 L525,174 C320,225 170,282 0,275 Z" fill="#7b2b72"/>
    <path d="M0,275 C170,282 320,225 525,174 L525,300 L0,300 Z" fill="url(#warm)"/>
    <path d="M0,246 C90,250 170,238 232,218" stroke="#e8402e" stroke-width="4" fill="none"/>
    <path d="M330,200 C400,180 460,165 525,152" stroke="#e8402e" stroke-width="6" fill="none"/>
    <path d="M360,190 C420,176 470,167 525,160" stroke="#f07a22" stroke-width="3" fill="none"/>
  </svg>
  <h1 class="doctor-name">Dr. Lumi Harcourt</h1>
  <p class="credentials">M.B.B.S., F.C.G.F.C</p>
  <p class="role">Family General Practitioner</p>
  <p class="tagline">Caring about your health</p>
  <div class="guild-mark"><span class="dot"></span>CGFC</div>
</section>

<section class="card card--opt1" aria-label="Card back, option 1">
  <div class="faint-mark" aria-hidden="true">CGFC</div>
  <h2 class="hours-title">Working Hours</h2>
  <ul class="hours">
    <li>Monday&nbsp;&nbsp; 7 AM &nbsp;- 7 PM</li>
    <li>Tuesday&nbsp; 7 AM - 12 PM</li>
    <li>Wednesday&nbsp; 7 AM - 10 PM</li>
    <li>Thursday&nbsp; 7 AM - 12 PM</li>
    <li>Friday &nbsp;&nbsp;7 AM &nbsp;- 8 PM</li>
    <li>Saturday&nbsp; 8 AM - 10 PM</li>
    <li>Sunday - Off</li>
  </ul>
  <div class="contact-band">
    <p>Level 2, Linden Arcade, Harbourview Plaza<br>Wattle Ridge, NSW 2987</p>
    <p class="phones"><span>P: 02 5550 1400</span><span class="sep"></span><span>F: 02 5550 1233</span></p>
  </div>
</section>

<section class="card card--opt2" aria-label="Card back, option 2">
  <div class="faint-mark" aria-hidden="true">CGFC</div>
  <h2 class="hours-title">Working Hours</h2>
  <ul class="hours">
    <li><span class="day">Monday</span><span class="time">7 AM &nbsp;- 7 PM</span></li>
    <li><span class="day">Tuesday</span><span class="time">7 AM - 12 PM</span></li>
    <li><span class="day">Wednesday</span><span class="time">7 AM - 10 PM</span></li>
    <li><span class="day">Thursday</span><span class="time">7 AM - 12 PM</span></li>
    <li><span class="day">Friday</span><span class="time">7 AM &nbsp;- 8 PM</span></li>
    <li><span class="day">Saturday</span><span class="time">8 AM - 10 PM</span></li>
    <li><span class="day">Sunday</span><span class="time">OFF</span></li>
  </ul>
  <div class="contact-band">
    <p>Level 2, Linden Arcade, Harbourview Plaza<br>Wattle Ridge, NSW 2987</p>
    <p class="phones"><span>P: 02 5550 1400</span><span class="sep"></span><span>F: 02 5550 1233</span></p>
  </div>
</section>

<section class="card card--opt3" aria-label="Card back, option 3">
  <div class="faint-mark" aria-hidden="true">CGFC</div>
  <h2 class="hours-title">Working Hours</h2>
  <ul class="hours">
    <li>Monday&nbsp; <span class="time">7 AM &nbsp;- 7 PM</span></li>
    <li>Tuesday&nbsp; <span class="time">7 AM - 12 PM</span></li>
    <li>Wednesday&nbsp; <span class="time">7 AM - 10 PM</span></li>
    <li>Thursday&nbsp; <span class="time">7 AM - 12 PM</span></li>
    <li>Friday&nbsp;&nbsp;&nbsp; <span class="time">7 AM &nbsp;- 8 PM</span></li>
    <li>Saturday&nbsp; <span class="time">8 AM - 10 PM</span></li>
    <li>Sunday - <span class="time">OFF</span></li>
  </ul>
  <div class="contact-band">
    <p>Level 2, Linden Arcade, Harbourview Plaza<br>Wattle Ridge, NSW 2987</p>
    <p class="phones"><span>P: 02 5550 1400</span><span class="sep"></span><span>F: 02 5550 1233</span></p>
  </div>
</section>

<p class="option-label" style="left:822px;top:338px;">Option# 1</p>
<p class="option-label" style="left:254px;top:680px;">Option# 2</p>
<p class="option-label" style="left:819px;top:687px;">Option# 3</p>

</body>
</html>
```